Like dislike neutral indicator

I need to design a like indicator to show how many people like the idea.
Also 3 buttons for Don't like, Neutral, I like it.

It would be a bonus if you can provide the design for other elements in the page too. Please see the image attached.

```html
<!DOCTYPE html>
<html lang="en">
<head>
<meta charset="utf-8">
<title>Do you like this idea?</title>
<link rel="stylesheet" href="https://fonts.googleapis.com/css2?family=Roboto+Condensed:wght@400;700&display=swap">
<style>
  :root {
    --bg: #ffffff;
    --ink: #222222;
    --no: #c4242b;
    --no-dark: #9c1b21;
    --neutral: #5b3383;
    --neutral-dark: #43235f;
    --yes: #34499a;
    --yes-dark: #263873;
    --dislike-band: #d5683a;
    --dislike-band-light: #eab29b;
    --like-band: #4b5fa9;
    --like-band-light: #a7aed3;
    --arrow: #ffffff;
  }
  html, body {
    margin: 0;
    padding: 0;
    overflow: hidden;
    background: var(--bg);
  }
  .canvas {
    position: relative;
    width: 1200px;
    height: 1000px;
    background: var(--bg);
    overflow: hidden;
    font-family: "Roboto Condensed", "Arial Narrow", sans-serif;
    color: var(--ink);
  }
  .graphics {
    position: absolute;
    inset: 0;
  }
  .question {
    position: absolute;
    left: 0;
    width: 1200px;
    top: 412px;
    margin: 0;
    text-align: center;
    font-weight: 700;
    font-size: 128px;
    line-height: 1;
    letter-spacing: -3px;
    transform: scaleX(0.86);
    transform-origin: 592px 0;
  }
  .vote-label {
    position: absolute;
    top: 792px;
    margin: 0;
    font-weight: 400;
    font-size: 76px;
    line-height: 1;
    letter-spacing: -1px;
    transform: translateX(-50%) scaleX(0.82);
  }
  .vote-label--no { left: 366px; }
  .vote-label--neutral { left: 560px; }
  .vote-label--yes { left: 836px; }
</style>
</head>
<body>
<main class="canvas">
  <svg class="graphics" width="1200" height="1000" viewBox="0 0 1200 1000" aria-hidden="true">
    <defs>
      <radialGradient id="no-fill" cx="50%" cy="45%" r="55%">
        <stop offset="0.8" stop-color="var(--no)"/>
        <stop offset="1" stop-color="var(--no-dark)"/>
      </radialGradient>
      <radialGradient id="neutral-fill" cx="50%" cy="45%" r="55%">
        <stop offset="0.8" stop-color="var(--neutral)"/>
        <stop offset="1" stop-color="var(--neutral-dark)"/>
      </radialGradient>
      <radialGradient id="yes-fill" cx="50%" cy="45%" r="55%">
        <stop offset="0.8" stop-color="var(--yes)"/>
        <stop offset="1" stop-color="var(--yes-dark)"/>
      </radialGradient>
      <linearGradient id="dislike-band" x1="0" y1="0" x2="0" y2="1">
        <stop offset="0" stop-color="var(--dislike-band)"/>
        <stop offset="0.5" stop-color="var(--dislike-band-light)"/>
        <stop offset="1" stop-color="var(--dislike-band)"/>
      </linearGradient>
      <linearGradient id="like-band" x1="0" y1="0" x2="0" y2="1">
        <stop offset="0" stop-color="var(--like-band)"/>
        <stop offset="0.5" stop-color="var(--like-band-light)"/>
        <stop offset="1" stop-color="var(--like-band)"/>
      </linearGradient>
      <filter id="arrow-shadow" x="-20%" y="-20%" width="150%" height="150%">
        <feDropShadow dx="3" dy="3" stdDeviation="2" flood-color="#000" flood-opacity="0.45"/>
      </filter>

      <path id="arrow-down" d="M-30,-58 H30 Q33,-58 33,-55 V2 H47 Q55,3 50,11 L4,56 Q0,59 -4,56 L-50,11 Q-55,3 -47,2 H-33 V-55 Q-33,-58 -30,-58 Z"/>
      <path id="arrow-up" d="M-30,58 H30 Q33,58 33,55 V-2 H47 Q55,-3 50,-11 L4,-56 Q0,-59 -4,-56 L-50,-11 Q-55,-3 -47,-2 H-33 V55 Q-33,58 -30,58 Z"/>
      <g id="arrow-pair">
        <path d="M-49,-42 H-21 Q-18,-42 -18,-39 V0 H-10 Q-5,1 -9,6 L-32,29 Q-35,31 -38,29 L-61,6 Q-65,1 -59,0 H-52 V-39 Q-52,-42 -49,-42 Z"/>
        <path d="M11,40 H39 Q42,40 42,37 V-2 H50 Q55,-3 51,-8 L28,-31 Q25,-33 22,-31 L-1,-8 Q-5,-3 1,-2 H8 V37 Q8,40 11,40 Z"/>
      </g>
    </defs>

    <!-- sentiment meter -->
    <g class="meter">
      <path class="meter-band meter-band--dislike" d="M219,208 L381,222 Q371,253 381,284 L219,298 Q245,253 219,208 Z" fill="url(#dislike-band)"/>
      <path class="meter-band meter-band--like" d="M692,223 L980,208 Q954,254 980,300 L692,287 Q703,255 692,223 Z" fill="url(#like-band)"/>

      <g class="meter-dot meter-dot--no" transform="translate(139 253)">
        <circle r="75" fill="url(#no-fill)"/>
        <use href="#arrow-down" fill="var(--arrow)" filter="url(#arrow-shadow)" transform="scale(0.92)"/>
      </g>
      <g class="meter-dot meter-dot--neutral" transform="translate(608 253)">
        <circle r="75" fill="url(#neutral-fill)"/>
        <use href="#arrow-pair" fill="var(--arrow)" filter="url(#arrow-shadow)" transform="scale(0.92)"/>
      </g>
      <g class="meter-dot meter-dot--yes" transform="translate(1059 254)">
        <circle r="75" fill="url(#yes-fill)"/>
        <use href="#arrow-up" fill="var(--arrow)" filter="url(#arrow-shadow)" transform="scale(0.92)"/>
      </g>
    </g>

    <!-- vote buttons -->
    <g class="vote-buttons">
      <g class="vote-button vote-button--no" transform="translate(378 683)">
        <circle r="82" fill="url(#no-fill)"/>
        <use href="#arrow-down" fill="var(--arrow)" filter="url(#arrow-shadow)"/>
      </g>
      <g class="vote-button vote-button--neutral" transform="translate(609 683)">
        <circle r="82" fill="url(#neutral-fill)"/>
        <use href="#arrow-pair" fill="var(--arrow)" filter="url(#arrow-shadow)"/>
      </g>
      <g class="vote-button vote-button--yes" transform="translate(836 683)">
        <circle r="82" fill="url(#yes-fill)"/>
        <use href="#arrow-up" fill="var(--arrow)" filter="url(#arrow-shadow)"/>
      </g>
    </g>
  </svg>

  <h1 class="question">Do you like this idea?</h1>
  <p class="vote-label vote-label--no">NO</p>
  <p class="vote-label vote-label--neutral">NEUTRAL</p>
  <p class="vote-label vote-label--yes">YES</p>
</main>
</body>
</html>
```